Medical Skincare services/menu/pricing Booklet 12 pages

We need produce a 12-page glossy, saddle-stitched booklet (5 1/2" tall X 81/2" wide). The booklet will be used as a services menu for a skin care salon. I have mocked up the booklet (w/ all copy) in WORD and I've provided a separate PDF of the accurate page order (see files attached). IMPORTANT: Feel free to use your creativity yet style-wise it should kinda match my wife's website colors and text style. Her clients are demanding so she wants a clean, high end, modern look (ala Apple maybe?). See her website for a frame of reference www.GlowWithMira.com

Target Market(s)

upscale female, professional women, teens with acne

Industry/Entity Type

Medical

Requirements
Must have
• the pics in the mock up are important. I've attached them here

```html
<!DOCTYPE html>
<html lang="en">
<head>
<meta charset="utf-8">
<title>Glow With Mira – Services Booklet</title>
<link href="https://fonts.googleapis.com/css2?family=Open+Sans:ital,wght@0,400;0,600;0,700;0,800;1,400;1,700&family=Great+Vibes&display=swap" rel="stylesheet">
<style>
  :root {
    --backdrop: #b9b7ba;
    --cover-black: #050505;
    --white: #ffffff;
    --soft-grey: #c9c9c9;
    --ink: #1c1c1c;
    --body-ink: #3a3a3a;
    --lavender-top: #d9d5ec;
    --lavender-bottom: #f3f2f8;
    --tag-pink: #e9d2dc;
    --green-dark: #6dbd60;
    --green-light: #98cb8a;
  }
  * { box-sizing: border-box; margin: 0; padding: 0; }
  html, body { width: 1200px; height: 850px; overflow: hidden; }
  body {
    background: var(--backdrop);
    font-family: "Open Sans", Arial, sans-serif;
    position: relative;
  }
  .spread {
    position: absolute;
    left: 150px;
    width: 900px;
    height: 330px;
    display: flex;
    box-shadow: 0 6px 14px rgba(0,0,0,.25);
  }
  .spread--cover { top: 45px; }
  .spread--inside { top: 445px; }
  .page { position: relative; width: 450px; height: 330px; overflow: hidden; }

  /* Cover spread */
  .back-cover, .front-cover { background: var(--cover-black); color: var(--white); }
  .back-cover .portrait {
    position: absolute; left: 0; top: 0; width: 230px; height: 330px;
    background: linear-gradient(160deg, #e8e4e6 0%, #8a7c78 35%, #5b4e49 65%, #2a2625 100%);
  }
  .back-cover .owner-sign {
    position: absolute; left: 150px; bottom: 34px;
    font-family: "Great Vibes", cursive; font-size: 26px; color: var(--white);
  }
  .back-cover .owner-role {
    position: absolute; left: 175px; bottom: 20px; font-size: 8px; color: var(--soft-grey);
  }
  .contact {
    position: absolute; left: 250px; top: 18px; width: 180px;
    text-align: center; font-size: 9px; line-height: 1.25;
  }
  .contact .label { font-style: italic; }
  .contact .web { font-weight: 700; font-style: italic; font-size: 10px; }
  .contact .phone { font-weight: 700; font-style: italic; font-size: 12px; margin-bottom: 6px; }
  .contact .map {
    width: 110px; height: 60px; margin: 0 auto 6px;
    background: linear-gradient(135deg, #f4f4f4, #dcdcdc);
  }
  .contact .biz { font-weight: 700; font-style: italic; font-size: 12px; }
  .contact .hours-title { font-weight: 700; font-style: italic; margin-top: 6px; }
  .contact .hours { font-style: italic; font-size: 7.5px; line-height: 1.3; }
  .contact .pin { vertical-align: -1px; }

  .brand-mark {
    position: absolute; left: 36px; top: 104px;
    display: flex; align-items: center; gap: 10px;
  }
  .brand-mark .square { width: 16px; height: 16px; background: var(--white); flex: none; }
  .brand-mark .name {
    font-weight: 800; font-size: 32px; letter-spacing: 1px; color: var(--white);
    line-height: 1.05; white-space: nowrap;
  }
  .service-list {
    position: absolute; right: 28px; bottom: 22px;
    list-style: none; text-align: right;
    font-size: 12px; line-height: 1.3; color: var(--soft-grey);
  }

  /* Inside spread */
  .about-page { background: linear-gradient(180deg, var(--lavender-top), var(--lavender-bottom)); }
  .about-page .portrait {
    position: absolute; left: 0; top: 0; width: 120px; height: 330px;
    background: linear-gradient(180deg, #cfc9bf 0%, #9aa59a 40%, #7d8f96 70%, #6a6c63 100%);
  }
  .about-copy { position: absolute; left: 128px; top: 70px; width: 306px; color: var(--body-ink); }
  .about-copy h1 { font-size: 12px; font-weight: 700; color: var(--ink); margin-bottom: 4px; }
  .about-copy h2 {
    display: inline-block; font-size: 10px; font-weight: 600; color: var(--ink);
    background: var(--tag-pink); padding: 1px 6px; margin-bottom: 4px;
  }
  .about-copy p {
    font-size: 7.4px; line-height: 1.32; text-align: justify; margin-bottom: 10px;
  }
  .color-page { background: linear-gradient(90deg, var(--green-dark), var(--green-light)); }
</style>
</head>
<body>
  <section class="spread spread--cover">
    <div class="page back-cover">
      <div class="portrait" role="img" aria-label="Photo of the owner in a grey knit top and faux fur vest"></div>
      <div class="owner-sign">Mira Talbot</div>
      <div class="owner-role">Aesthetician &amp; Owner</div>
      <div class="contact">
        <div class="label">BOOK ONLINE</div>
        <div class="web">www.GlowWithMira.com</div>
        <div class="label">Or Call/Text</div>
        <div class="phone">(555) 014-2290</div>
        <div class="map" role="img" aria-label="Street map showing the studio location"></div>
        <div class="label">
          <svg class="pin" width="7" height="9" viewBox="0 0 7 9"><path d="M3.5 0a3.5 3.5 0 0 0-3.5 3.5C0 6 3.5 9 3.5 9S7 6 7 3.5A3.5 3.5 0 0 0 3.5 0z" fill="#fff"/></svg>
          LOCATION:</div>
        <div class="biz">Glow With Mira</div>
        <div>412 Aspen Ridge Rd #200</div>
        <div>Fairview, Colorado 80000</div>
        <div class="hours-title">BY APPT. HOURS:</div>
        <div class="hours">
          Monday 10:00am-4:00pm<br>
          Tuesday 10:00am-6:00pm<br>
          Wednesday 10:00am-6:00pm<br>
          Thursday 10:00am-6:00pm<br>
          Friday 10:00am-6:00pm<br>
          Saturday 10:00-4:00pm<br>
          Sunday: Closed
        </div>
      </div>
    </div>
    <div class="page front-cover">
      <div class="brand-mark">
        <span class="square"></span>
        <span class="name">GLOW WITH<br>MIRA</span>
      </div>
      <ul class="service-list">
        <li>HydraGlow Facial</li>
        <li>Laser Renewal</li>
        <li>IPL (Brightlight)</li>
        <li>Vascular</li>
        <li>Microneedling Pro</li>
        <li>LED Light Therapy</li>
        <li>Clarity Peel</li>
        <li>Customized</li>
        <li>Facials &amp; Peels</li>
        <li>Dermaplane</li>
      </ul>
    </div>
  </section>

  <section class="spread spread--inside">
    <div class="page about-page">
      <div class="portrait" role="img" aria-label="Photo of the owner in a long patterned dress beside a flower planter"></div>
      <div class="about-copy">
        <h1>Mira Talbot</h1>
        <h2>Medical Aesthetician &amp; Owner</h2>
        <p>As a teenager, I had cystic acne so bad that I would ditch school to swim in the ocean because the salt water seemed to dry out and heal my skin. I was on such a mission to clear my skin that I spent my weekly allowance on skin care products I saw on TV. Then, I memorized every ingredient. I was so intrigued by the beauty industry that, by 19, I began a career as a make up artist for Lumière, Novaa, Belle Rose, Kestrel, and Opaline. By 23, I was a skincare consultant for the Vivienne Roche Salons in Beverly Hills and Orange County California. I was honored to learn from the world's most demanding clients.</p>
        <h2>I Understand Why Your Skin Matters</h2>
        <p>Admit it. We take more pictures of ourselves than ever…and then try to "fix" our blemishes with photo filters. I understand your frustrations. Some of you know I've had a parallel career as a professional singer with dozens of network TV appearances; where the HD cameras take extreme close ups…Yikes!). I also sing the National Anthem at pro football, basketball, and baseball games, where their 200 foot-wide stadium video screens constantly remind me that skin imperfections are magnified. I will help get your skin more naturally beautiful so you can use less photo filters.</p>
      </div>
    </div>
    <div class="page color-page"></div>
  </section>
</body>
</html>
```